Bref créative |
Wordpress Website for Law Office | ||
Law Offices of Dorian Thackeray | ||
Law | ||
www.dthackerlegal.example | ||
Law Offices | ||
Clean/Simple Professional Content Driven Friendly Academic Sophisticated Elegant Service Oriented Traditional |
top | ||
www.dthackerlegal.example/logo.pdf | ||
I want my current website, dthackerlegal.example, redesigned using my logo, http://www.dthackerlegal.example/logo.pdf. The menus will be the same. The content will be the same. The layout should be similar. All I am looking for is a new design. Once the design is selected, the wordpress theme will be created based on it. |

```html
<!DOCTYPE html>
<html lang="en">
<head>
<meta charset="utf-8">
<title>Law Offices of Dorian Thackeray</title>
<link href="https://fonts.googleapis.com/css2?family=Cinzel:wght@400;600&family=Open+Sans:wght@400;600;700&display=swap" rel="stylesheet">
<style>
:root{
  --navy:#163f73;
  --navy-dark:#0f2f58;
  --blue:#2a62a8;
  --link:#2a62a8;
  --page:#e6e9ed;
  --panel:#ffffff;
  --box:#d9dee4;
  --box-edge:#c4cbd3;
  --text:#333a44;
  --muted:#6a7380;
  --grey-head:#6f7780;
}
*{box-sizing:border-box;margin:0;padding:0}
html,body{width:1200px;height:1023px;overflow:hidden}
body{background:var(--page);font-family:"Open Sans",Arial,sans-serif;color:var(--text);position:relative}
.topbar{height:28px;background:linear-gradient(var(--navy),var(--navy-dark))}
.topbar .inner{width:950px;margin:0 auto;display:flex;justify-content:flex-start;padding-left:30px}
.tollfree{font-family:"Cinzel",serif;font-weight:600;color:#fff;font-size:19px;line-height:28px;letter-spacing:.5px}
.tollfree span{font-size:13px;margin-right:6px}
.wrap{width:950px;margin:0 auto;position:relative}
.header{height:139px;position:relative}
.brand{position:absolute;left:10px;top:38px;display:flex;align-items:center;gap:14px}
.brand .mark{width:54px;height:54px;background:var(--navy)}
.brand .name{font-family:"Cinzel",serif;font-weight:600;font-size:30px;color:var(--navy);line-height:1.05;width:330px}
.scales{position:absolute;left:625px;top:6px;width:150px;height:130px;border-radius:50% 50% 8px 8px;background:radial-gradient(circle at 50% 40%,#f4f5f7,#b9c0c8 70%,#9aa3ad)}
.utility{position:absolute;right:0;top:16px;list-style:none}
.utility li{display:flex;align-items:center;gap:6px;height:22px;margin-bottom:4px;width:158px;padding:0 6px;border:1px solid #c7ccd3;background:linear-gradient(#fff,#eceff2);font-size:10.5px;color:var(--text)}
.utility li i{width:13px;height:13px;background:var(--blue);border-radius:2px;display:block}
.nav{height:41px;background:linear-gradient(#2b5d9a,var(--navy));display:flex;align-items:center;padding-left:10px;border-radius:3px 3px 0 0}
.nav a{color:#fff;text-decoration:none;font-size:12.5px;font-weight:600;padding:0 18px;line-height:41px;border-right:1px solid rgba(255,255,255,.2)}
.nav a.active{background:rgba(255,255,255,.15)}
.content{background:var(--panel);height:417px;display:flex;padding:18px 22px 0 18px;gap:32px}
.main{width:555px}
.main h1{font-family:"Cinzel",serif;font-weight:600;font-size:25px;color:#222;display:flex;align-items:center;gap:10px;margin-bottom:14px}
.main h1 i{width:22px;height:22px;background:var(--navy);display:block}
.main p{font-size:11.4px;line-height:1.55;margin-bottom:12px}
.main a{color:var(--link)}
.ticks{list-style:none;margin:6px 0 12px}
.ticks li{display:flex;gap:8px;font-size:11.4px;line-height:1.5;margin-bottom:10px;align-items:flex-start}
.ticks svg{flex:none;margin-top:1px}
.side{width:310px}
.side h2{background:linear-gradient(#8a929c,var(--grey-head));color:#fff;font-family:"Cinzel",serif;font-weight:400;font-size:22px;height:40px;display:flex;align-items:center;gap:10px;padding-left:10px;border-radius:3px 3px 0 0}
.side h2 i{width:20px;height:20px;border-radius:50%;background:#fff;display:block}
.side .intro{font-size:11.4px;line-height:1.5;padding:10px 4px}
.areas{list-style:none;border-top:1px solid #e2e5e9}
.areas li{display:flex;align-items:center;gap:12px;height:40px;border-bottom:1px solid #e2e5e9;padding-left:12px;font-size:12.5px;font-weight:700;color:var(--link)}
.areas li i{width:18px;height:18px;background:var(--blue);border-radius:3px;display:block}
.side .note{font-size:11.4px;line-height:1.5;padding:10px 4px}
.side .note a{color:var(--link)}
.offices{height:250px;background:linear-gradient(#eef0f3,#dfe3e8);display:grid;grid-template-columns:repeat(3,278px);column-gap:22px;row-gap:20px;padding:22px 0 0 42px}
.office{height:100px;background:linear-gradient(#e8ebee,var(--box));border:1px solid var(--box-edge);border-radius:4px;text-align:center;padding-top:8px}
.office h3{font-family:"Cinzel",serif;font-weight:600;font-size:17px;color:var(--blue);margin-bottom:5px}
.office p{font-size:10.5px;line-height:1.45;color:var(--text)}
.footer{position:absolute;left:0;right:0;top:875px;height:148px;background:linear-gradient(var(--navy),var(--navy-dark))}
.footer .inner{width:950px;margin:0 auto;text-align:center;color:#dfe7f2}
.flinks{padding-top:14px;font-size:11px;font-weight:700}
.flinks a{color:#fff;text-decoration:none;margin:0 3px}
.fnote{font-size:10.5px;line-height:1.5;padding:14px 40px 0}
.fbottom{display:flex;justify-content:space-between;align-items:center;padding:20px 40px 0 120px;font-size:10.5px}
.fbottom a{color:#fff;text-decoration:none;margin-left:10px}
.social{display:flex;gap:4px}
.social i{width:13px;height:13px;background:#b9cbe2;display:block;border-radius:2px}
</style>
</head>
<body>
<div class="topbar"><div class="inner"><div class="tollfree"><span>CALL TOLL FREE</span>(800) 555-0142</div></div></div>

<div class="wrap">
  <header class="header">
    <div class="brand"><div class="mark"></div><div class="name">Law Offices of Dorian Thackeray</div></div>
    <div class="scales" role="img" aria-label="Illustration of scales of justice on a silver emblem"></div>
    <ul class="utility">
      <li><i></i>Join Our Mailing List</li>
      <li><i></i>Add This To Favorites</li>
      <li><i></i>Log Into My File 24/7</li>
      <li><i></i>Languages Spoken</li>
    </ul>
  </header>

  <nav class="nav">
    <a href="#">Home Page</a><a class="active" href="#">Practice Areas</a><a href="#">Why Us</a><a href="#">Our Fees</a><a href="#">Free Advice</a><a href="#">Contact Us</a><a href="#">Closing Tips</a><a href="#">Languages</a>
  </nav>

  <section class="content">
    <div class="main">
      <h1><i></i>Welcome to our site</h1>
      <p>The Law Offices of Dorian Thackeray is dedicated to providing the highest quality legal advice and counseling to clients throughout New York State. We offer extensive knowledge and experience in <a href="#">Real Estate</a> and <a href="#">Business Law</a>.</p>
      <p>When faced with a legal question, choosing the right law firm is a critical first step in resolving the issue. By choosing the Law Offices of Dorian Thackeray, you are choosing a firm that:</p>
      <ul class="ticks">
        <li><svg width="14" height="14" viewBox="0 0 14 14"><rect width="14" height="14" rx="2" fill="#2a62a8"/><path d="M3 7l3 3 5-6" stroke="#fff" stroke-width="2" fill="none"/></svg>Provides individualized service that gives its clients confidence and peace of mind.</li>
        <li><svg width="14" height="14" viewBox="0 0 14 14"><rect width="14" height="14" rx="2" fill="#2a62a8"/><path d="M3 7l3 3 5-6" stroke="#fff" stroke-width="2" fill="none"/></svg>Possesses vast experience and resources that enables it to handle your legal needs in a professional manner with efficiency, clarity, and resolve.</li>
        <li><svg width="14" height="14" viewBox="0 0 14 14"><rect width="14" height="14" rx="2" fill="#2a62a8"/><path d="M3 7l3 3 5-6" stroke="#fff" stroke-width="2" fill="none"/></svg>Charges reasonable and straight-forward prices for the legal services rendered.</li>
      </ul>
      <p>Individuals and business entities alike have placed their trust in the Law Offices of Dorian Thackeray for one simple reason: they know they will be represented by highly skilled and dedicated attorneys who provide a level of sophistication and a value proposition that is unmatched. Please take a moment to browse through our website to learn how we can help you.</p>
    </div>
    <aside class="side">
      <h2><i></i>Practice Areas</h2>
      <p class="intro">We have extensive experience in the areas of law listed below.</p>
      <ul class="areas">
        <li><i></i>Business Law</li>
        <li><i></i>Internet Law</li>
        <li><i></i>Real Estate Law</li>
        <li><i></i>Wills &amp; Trusts Law</li>
      </ul>
      <p class="note">Please click on the link above for a detailed description of each practice area.<br>If you need representation in any area of law not listed above, please <a href="#">contact us</a>. We have many experienced attorneys that we work with and we will be happy to refer you to an attorney who can handle your matter.</p>
    </aside>
  </section>

  <section class="offices">
    <div class="office"><h3>Brooklyn Office</h3><p>1840 Harbor Lane, 2nd Floor<br>Brooklyn, NY 11235<br>(718) 555-0123</p></div>
    <div class="office"><h3>Manhattan Office</h3><p>415 Mercer Avenue, Suite 1405<br>New York, NY 10001<br>(212) 555-0167</p></div>
    <div class="office"><h3>Long Island Office</h3><p>52 Birchwood Road<br>Great Neck, NY 11021<br>(516) 555-0188</p></div>
    <div class="office"><h3>Westchester Office</h3><p>310 Elm Street, 4th Floor<br>White Plains, NY 10601<br>(914) 555-0139</p></div>
    <div class="office"><h3>Staten Island Office</h3><p>Coming Soon<br>Coming Soon<br>Coming Soon</p></div>
    <div class="office"><h3>New Jersey Office</h3><p>Coming Soon<br>Coming Soon<br>Coming Soon</p></div>
  </section>
</div>

<footer class="footer">
  <div class="inner">
    <div class="flinks"><a href="#">Home</a>| <a href="#">Practice</a>| <a href="#">Areas</a>| <a href="#">Why Us</a>| <a href="#">Our Fees</a>| <a href="#">Free Advice</a>| <a href="#">Closing Tips</a>| <a href="#">Contact Us</a>| <a href="#">Languages</a></div>
    <p class="fnote">Our attorneys provide legal services throughout the five boroughs of New York City (Brooklyn, Manhattan, Queens, Staten Island, and the Bronx), Long Island (both Nassau &amp; Suffolk), Westchester County and Upstate New York. This website constitutes attorney advertising.</p>
    <div class="fbottom">
      <span>© 2012 New York Real Estate Attorney, All Rights Reserved</span>
      <span><a href="#">Disclaimer</a> | <a href="#">Privacy Policy</a> | <a href="#">Site Map</a></span>
      <span class="social"><i></i><i></i><i></i><i></i><i></i></span>
    </div>
  </div>
</footer>
</body>
</html>
```